The Best Real Estate Post Card Ever

Create a memorable and attention grabbing postcard BACK to be used the same every month and sent to 20,000 homes. The front of the postcard will change, I will make this every month. But the back I want to be known as ME and when people see it after years they instantly think of ME. This is all about branding and getting to be known as the agent to call when they need to move. I have attached styles I have used on past marketing. This design must work with both 11x8.5 and 9x6 and allow room for the postage to flow nicely.

Target Market(s)

Luxury waterfront clients

Colors
ec1f27
0255a3
ffffff

Requirements
Must have
• Clean and modern, luxury feel to it.
Nice to have
• Attention grabbing way to be remembered.
Should not have
• cheap look

```html
<!DOCTYPE html>
<html lang="en">
<head>
<meta charset="utf-8">
<title>Marcus Delano — Postcard Back</title>
<link href="https://fonts.googleapis.com/css2?family=Libre+Baskerville:wght@700&family=Roboto:ital,wght@0,400;0,700;0,900;1,700;1,900&display=swap" rel="stylesheet">
<style>
  :root {
    --brand-red: #ec1f27;
    --brand-blue: #0255a3;
    --white: #ffffff;
    --ink: #1f1f1f;
    --photo-dark: #3e4650;
    --photo-light: #c9ccd0;
  }
  html, body { margin: 0; padding: 0; overflow: hidden; background: var(--white); }
  .postcard {
    position: relative;
    width: 1200px;
    height: 852px;
    overflow: hidden;
    background: var(--white);
    font-family: "Roboto", Arial, sans-serif;
    color: var(--ink);
  }
  .backdrop { position: absolute; inset: 0; }
  .brand-mark {
    position: absolute;
    left: 24px;
    top: 44px;
    width: 220px;
    display: flex;
    align-items: center;
    gap: 10px;
  }
  .brand-mark .dot {
    width: 30px; height: 30px; border-radius: 50%;
    background: var(--brand-red); flex: none;
  }
  .brand-mark .brand-name {
    font-family: "Libre Baskerville", Georgia, serif;
    font-weight: 700;
    font-size: 22px;
    line-height: 1.15;
    color: var(--brand-blue);
  }
  .agent-name {
    position: absolute;
    left: 262px;
    top: 50px;
    margin: 0;
    font-family: "Libre Baskerville", Georgia, serif;
    font-weight: 700;
    font-size: 30px;
    color: var(--brand-blue);
  }
  .contact-block {
    position: absolute;
    left: 20px;
    top: 190px;
    font-size: 16px;
    line-height: 1.2;
    color: var(--ink);
  }
  .contact-block p { margin: 0; }
  .address-area {
    position: absolute;
    left: 470px;
    top: 120px;
    width: 380px;
    height: 190px;
  }
  .guarantee-title {
    position: absolute;
    left: 24px;
    top: 340px;
    margin: 0;
    font-weight: 900;
    font-size: 40px;
    line-height: 1;
    color: var(--brand-blue);
  }
  .guarantee-stars { position: absolute; left: 152px; top: 336px; }
  .guarantee-promise {
    position: absolute;
    left: 312px;
    top: 346px;
    margin: 0;
    font-style: italic;
    font-weight: 900;
    font-size: 29px;
    line-height: 1.15;
    color: var(--brand-red);
  }
  .highlights {
    position: absolute;
    left: 522px;
    top: 432px;
    margin: 0;
    padding-left: 22px;
    font-size: 21px;
    line-height: 31px;
    color: var(--ink);
  }
  .agent-photo {
    position: absolute;
    left: 94px;
    top: 452px;
    width: 350px;
    height: 400px;
    border-radius: 160px 160px 0 0;
    background: linear-gradient(180deg, var(--photo-light) 0%, var(--photo-dark) 100%);
  }
</style>
</head>
<body>
<div class="postcard">
  <svg class="backdrop" width="1200" height="852" viewBox="0 0 1200 852" aria-hidden="true">
    <path d="M560 0 C 760 50, 1010 120, 1200 380 L1200 0 Z" fill="var(--brand-red)"/>
    <path d="M0 598 C 300 560, 620 730, 900 712 S 1140 700 1200 706 L1200 852 L0 852 Z" fill="var(--brand-blue)"/>
    <path d="M0 590 C 300 552, 620 722, 900 704 S 1140 692 1200 698" fill="none" stroke="var(--white)" stroke-width="4"/>
  </svg>

  <div class="brand-mark">
    <span class="dot"></span>
    <span class="brand-name">Harborline Realty</span>
  </div>

  <h1 class="agent-name">Marcus Delano</h1>

  <div class="contact-block">
    <p>CRS, ABR, SRS, PSA, CLHMS, SFR, RSPS</p>
    <p>(555) 014-2286</p>
    <p>marcus@harborlinerealty.example</p>
    <p>social: TheDelanoGroup</p>
    <p>Realtor | Broker Associate Harborline Realty</p>
    <p>Vice President - Safe Shores Swim Fund INC</p>
  </div>

  <div class="address-area" aria-label="Clear space for mailing address and postage"></div>

  <h2 class="guarantee-title">5 Star<br>Guarantee</h2>
  <svg class="guarantee-stars" width="50" height="36" viewBox="0 0 50 36" aria-hidden="true">
    <g fill="var(--brand-red)">
      <polygon points="8,2 10,7 15,7 11,10 12.5,15 8,12 3.5,15 5,10 1,7 6,7"/>
      <polygon points="25,2 27,7 32,7 28,10 29.5,15 25,12 20.5,15 22,10 18,7 23,7"/>
      <polygon points="42,2 44,7 49,7 45,10 46.5,15 42,12 37.5,15 39,10 35,7 40,7"/>
      <polygon points="16,19 18,24 23,24 19,27 20.5,32 16,29 11.5,32 13,27 9,24 14,24"/>
      <polygon points="34,19 36,24 41,24 37,27 38.5,32 34,29 29.5,32 31,27 27,24 32,24"/>
    </g>
  </svg>
  <p class="guarantee-promise">If I Don't Meet Your Expectations,<br>You Don't Pay Me</p>

  <ul class="highlights">
    <li>200+ 5 Star Searchly Reviews</li>
    <li>Coral Bay County Resident 20+ Years</li>
    <li>Certified Luxury Home Marketing Specialist</li>
    <li>Available 7 Days a Week From 8 AM Till Midnight</li>
    <li>$20,000,000+ In Pending/Sold Sales So Far In 2021</li>
    <li>Professional Photography Included With Every Listing</li>
    <li>Hassle Free Listing Agreements, Cancel Anytime with No Fees</li>
  </ul>

  <div class="agent-photo" role="img" aria-label="Portrait of the agent holding his young son"></div>
</div>
</body>
</html>
```